Project Manager Business Card for Top Architectural Firm

Update and design a stunning Senior Project Manager Business Card

MARCO T. DRUMMOND II
Senior Project Manager

H A L C Y O N
A R C H I T E C T U R E L L C.
www.HalcyonGrandEstates.example
4127 NW 52nd Ter. Suite 2308
Miami, FL 33148
C: (305) 555-0184
mdrummond.halcyongrandestates@mailbox.example

Looking to have the logo to be UV Spot ink printed and to be prominent.

Target Market(s)

High end real estate architecture construction

Industry/Entity Type

Architect

Contact Information for Business Card

MARCO T. DRUMMOND II
Senior Project Manager

H A L C Y O N
Miami, FL 33148
C: (305) 555-0184

Font styles to use
Sans Serif

Colors

Designer to choose colors to be used in the design.

Requirements
Must have
• Prominent Logo

```html
<!DOCTYPE html>
<html lang="en">
<head>
<meta charset="utf-8">
<title>Halcyon Architecture – Business Card</title>
<link rel="stylesheet" href="https://fonts.googleapis.com/css2?family=Montserrat:wght@300;400;600;700&display=swap">
<style>
  :root {
    --stage: #1b1b1b;
    --card-black: #141414;
    --card-white: #ffffff;
    --ink-white: #f2f2f2;
    --ink-soft: #cfcfcf;
    --ink-black: #111111;
    --gloss: #3a3a3a;
    --web-grey: #2c2c2c;
    --mark-blue: #2f8fc9;
  }
  * { margin: 0; padding: 0; box-sizing: border-box; }
  html, body { width: 1200px; height: 900px; overflow: hidden; }
  body {
    background: var(--stage);
    font-family: "Montserrat", sans-serif;
    position: relative;
  }
  .card {
    position: absolute;
    left: 320px;
    width: 560px;
    height: 320px;
    border-radius: 16px;
    overflow: hidden;
    box-shadow: 0 14px 30px rgba(0,0,0,.55);
  }
  /* Back side */
  .card-back { top: 100px; background: var(--card-black); }
  .card-back .brand {
    position: absolute;
    left: 0; right: 0; top: 88px;
    display: flex; flex-direction: column; align-items: center;
    color: var(--gloss);
  }
  .brand-dot {
    width: 46px; height: 46px; border-radius: 50%;
    background: currentColor;
    margin-bottom: 14px;
  }
  .brand-name {
    font-weight: 300;
    font-size: 46px;
    letter-spacing: 12px;
    line-height: 1;
    padding-left: 12px;
  }
  .brand-sub {
    font-weight: 300;
    font-size: 12px;
    letter-spacing: 6px;
    margin-top: 8px;
    padding-left: 6px;
  }
  .card-back .website {
    position: absolute;
    left: 0; right: 0; bottom: 42px;
    text-align: center;
    font-size: 12px;
    font-weight: 600;
    letter-spacing: 2.5px;
    color: var(--web-grey);
  }
  /* Front side */
  .card-front { top: 480px; background: var(--card-black); }
  .front-brand-panel {
    position: absolute; left: 0; top: 0; bottom: 0;
    width: 232px;
    background: var(--card-white);
    display: flex; flex-direction: column; align-items: center; justify-content: center;
    color: var(--ink-black);
  }
  .front-brand-panel .brand-dot {
    width: 40px; height: 40px;
    background: var(--mark-blue);
    margin-bottom: 16px;
  }
  .front-brand-panel .brand-name { font-size: 30px; letter-spacing: 7px; padding-left: 7px; }
  .front-brand-panel .brand-sub { font-size: 8.5px; letter-spacing: 3.4px; margin-top: 8px; padding-left: 3px; }
  .contact {
    position: absolute; left: 232px; right: 0; top: 0; bottom: 0;
    padding: 32px 24px 30px 22px;
    color: var(--ink-white);
    display: flex; flex-direction: column;
  }
  .person { text-align: right; }
  .person-name { font-weight: 700; font-size: 16px; letter-spacing: -.2px; }
  .person-title { font-size: 11px; font-weight: 400; color: var(--ink-soft); margin-top: 3px; }
  .reach { text-align: right; margin-top: 46px; font-size: 11px; line-height: 1.7; }
  .firm { margin-top: auto; }
  .firm-name {
    font-weight: 700; font-size: 16px;
    padding-bottom: 4px;
    border-bottom: 1px solid var(--ink-white);
    display: inline-block;
  }
  .firm-address { font-size: 10.5px; margin-top: 5px; color: var(--ink-soft); }
</style>
</head>
<body>
  <section class="card card-back" aria-label="Business card, back">
    <div class="brand">
      <span class="brand-dot" aria-hidden="true"></span>
      <span class="brand-name">HALCYON</span>
      <span class="brand-sub">ARCHITECTURE LLC</span>
    </div>
    <p class="website">www.HalcyonGrandEstates.example</p>
  </section>

  <section class="card card-front" aria-label="Business card, front">
    <div class="front-brand-panel">
      <span class="brand-dot" aria-hidden="true"></span>
      <span class="brand-name">HALCYON</span>
      <span class="brand-sub">ARCHITECTURE LLC</span>
    </div>
    <div class="contact">
      <div class="person">
        <p class="person-name">MARCO T. DRUMMOND II</p>
        <p class="person-title">(Senior Project Manager)</p>
      </div>
      <div class="reach">
        <p>(305) 555-0184</p>
        <p>mdrummond.halcyongrandestates@mailbox.example</p>
      </div>
      <div class="firm">
        <p class="firm-name">HALCYON ARCHITECTURE LLC</p>
        <p class="firm-address">4127 NW 52nd Ter. Suite 2308 Miami, FL 33148</p>
      </div>
    </div>
  </section>
</body>
</html>
```